Grandpa Turnip's Valley Harvest Delivery

Two-sided postcard.

Front side: Can be a photo of available products. Need at least a 2" x 4" space to speak to the recipient and let them know who the post card is for and who it is from.

Back side: We will apply a sticker for the delivery address and space should be included for stamp.

```html
<!DOCTYPE html>
<html lang="en">
<head>
<meta charset="utf-8">
<title>Grandpa Turnip's Valley Harvest Delivery – Postcard</title>
<link rel="stylesheet" href="https://fonts.googleapis.com/css2?family=Kaushan+Script&family=Montserrat:wght@400;600;700&display=swap">
<style>
  :root {
    --backdrop: #5b5d5f;
    --card: #eef0f1;
    --card-edge: #dfe2e4;
    --green: #3d9230;
    --green-dark: #2f7524;
    --ink: #3a3a3a;
    --rule: #8d9194;
    --produce-a: #c9a25a;
    --produce-b: #c0452e;
    --produce-c: #6c8f3a;
  }
  * { box-sizing: border-box; margin: 0; padding: 0; }
  html, body {
    width: 896px; height: 1200px; overflow: hidden;
    background: var(--backdrop);
    font-family: "Montserrat", sans-serif;
    color: var(--ink);
  }
  .postcard {
    position: absolute; left: 63px; width: 770px; height: 502px;
    background: linear-gradient(180deg, var(--card) 0%, var(--card-edge) 100%);
    box-shadow: 0 6px 18px rgba(0,0,0,.35);
  }
  .postcard--front { top: 60px; }
  .postcard--back { top: 634px; }

  .brand {
    position: absolute; display: flex; align-items: center; gap: 8px;
    font-weight: 700; font-size: 17px; color: var(--green);
  }
  .brand__dot { width: 22px; height: 22px; border-radius: 50%; background: var(--green); flex: none; }

  .front__brand { left: 150px; top: 46px; }
  .front__title {
    position: absolute; left: 28px; top: 128px;
    font-family: "Kaushan Script", cursive; font-size: 70px; color: var(--green); line-height: 1;
  }
  .front__subtitle {
    position: absolute; left: 170px; top: 214px;
    font-family: "Kaushan Script", cursive; font-size: 36px; color: var(--green-dark);
  }
  .front__tractor { position: absolute; left: 118px; top: 222px; }
  .invite {
    position: absolute; left: 62px; top: 318px; width: 340px;
    font-size: 12.5px; line-height: 25px;
  }
  .invite .blank { display: inline-block; border-bottom: 1px solid var(--rule); height: 14px; vertical-align: baseline; }
  .produce {
    position: absolute; left: 468px; top: 62px; width: 270px; height: 410px;
    border-radius: 6px;
    background: radial-gradient(circle at 45% 45%, var(--produce-b) 0%, var(--produce-a) 45%, var(--produce-c) 80%, #e6e2d6 100%);
  }
  .sketch { position: absolute; left: 420px; top: 20px; }

  .back__divider { position: absolute; left: 410px; top: 40px; width: 1px; height: 420px; background: var(--rule); }
  .back__brand { left: 120px; top: 62px; }
  .signup {
    position: absolute; left: 40px; top: 128px; width: 330px; text-align: center;
  }
  .signup__title { font-family: "Kaushan Script", cursive; font-size: 62px; color: var(--green); line-height: 1; }
  .signup__body { font-size: 17px; line-height: 24px; margin-top: 8px; }
  .signup__free { font-family: "Kaushan Script", cursive; font-size: 46px; color: var(--green); margin-top: 10px; line-height: 1.1; }
  .signup__note { font-size: 14px; margin-top: 6px; }
  .contact { margin-top: 18px; font-size: 11px; line-height: 20px; display: flex; flex-direction: column; align-items: center; }
  .contact span { display: flex; align-items: center; gap: 6px; }
  .stamp-box { position: absolute; left: 650px; top: 30px; width: 92px; height: 78px; border: 1.5px solid var(--rule); }
  .address-line { position: absolute; left: 440px; width: 300px; height: 1px; background: var(--rule); }
</style>
</head>
<body>
  <section class="postcard postcard--front">
    <div class="brand front__brand"><span class="brand__dot"></span>Grandpa Turnip's</div>
    <h1 class="front__title">Farm to fork</h1>
    <svg class="front__tractor" width="44" height="30" viewBox="0 0 44 30" fill="none" stroke="#555" stroke-width="2">
      <rect x="12" y="6" width="14" height="12"/><path d="M26 12h12v8"/>
      <circle cx="16" cy="22" r="6"/><circle cx="36" cy="24" r="4"/>
    </svg>
    <p class="front__subtitle">delivery service</p>
    <div class="invite">
      <p>Your neighbor <span class="blank" style="width:230px"></span></p>
      <p>on <span class="blank" style="width:110px"></span> has invited you to</p>
      <p>try a <strong>FREE BOX</strong> with no enrollment fee!</p>
      <p>To Redeem: <span class="blank" style="width:240px"></span></p>
    </div>
    <svg class="sketch" width="340" height="470" viewBox="0 0 340 470" fill="none" stroke="#333" stroke-width="2" stroke-linecap="round">
      <path d="M20 170l40 20M18 215l42 0M30 260l35-18M250 18l10-15M290 30l18-15M320 70l18-6"/>
      <path d="M20 320c20-10 30-30 40-40M52 276l8 4-4 8"/>
    </svg>
    <div class="produce" role="img" aria-label="Photo of hands holding a wooden crate of fresh vegetables: carrots, cucumber, peppers, tomatoes, potatoes and mushrooms"></div>
  </section>

  <section class="postcard postcard--back">
    <div class="brand back__brand"><span class="brand__dot"></span>Grandpa Turnip's</div>
    <div class="signup">
      <h2 class="signup__title">Sign up</h2>
      <p class="signup__body">for<br>deliveries from our<br>NC farm community and<br>get your first box for</p>
      <p class="signup__free">FREE!</p>
      <p class="signup__note">(enrollment fee waived)</p>
      <div class="contact">
        <span><svg width="12" height="9" viewBox="0 0 12 9" fill="none" stroke="#555"><rect x=".5" y=".5" width="11" height="8"/><path d="M.5 .5l5.5 4 5.5-4"/></svg>hello@grandpaturnips.com</span>
        <span><svg width="11" height="11" viewBox="0 0 11 11" fill="none" stroke="#555"><circle cx="5.5" cy="5.5" r="5"/><path d="M.5 5.5h10M5.5 .5c-3 3-3 7 0 10M5.5 .5c3 3 3 7 0 10"/></svg>grandpaturnips.com</span>
      </div>
    </div>
    <div class="back__divider"></div>
    <div class="stamp-box"></div>
    <div class="address-line" style="top:232px"></div>
    <div class="address-line" style="top:278px"></div>
    <div class="address-line" style="top:324px"></div>
    <div class="address-line" style="top:370px"></div>
  </section>
</body>
</html>
```